Graphic Design for a block-note A4 size

We need a graphic design for a simple block-note A4 size. The product consists of 50 sheets in VERTICAL A4 (21x29,7cm) size, simply glued on top, without cover. We would like to have proposals with double application: one for home users without a logo and one for professionals with an area "put your logo here".
The graphics should be simple and attractive, elegant and pleasant to keep on your desk.
The block-notes may have standard squares (5 or 10 mm) or stripes (10 mm spaced) on the background to make the writing easy.
Feel free to use your creativity, the only limit is the CMYK color space.

We will upload some block-note simple templates and 3D sample images to help you.

• The graphics should be simple and attractive, elegant and pleasant to keep on your desk.

• The block-notes may have standard squares (5 or 10 mm) or stripes (10 mm spaced) on the background to make the writing easy.

```html
<!DOCTYPE html>
<html lang="en">
<head>
<meta charset="UTF-8">
<title>Squared Block-Note A4</title>
<link rel="stylesheet" href="https://fonts.googleapis.com/css2?family=Archivo:wght@700&display=swap">
<style>
  :root {
    --header-red: #dc251f;
    --footer-red: #c0272d;
    --edge-dark: #333333;
    --grid-line: #3a3a3a;
    --paper: #ffffff;
    --brand-ink: #1a1a1a;
    --cell-w: 40.476px;
    --cell-h: 40.4px;
  }
  * { margin: 0; padding: 0; box-sizing: border-box; }
  html, body {
    width: 850px;
    height: 1200px;
    overflow: hidden;
    background: var(--paper);
  }
  .note-sheet {
    position: relative;
    width: 850px;
    height: 1200px;
    background: var(--paper);
    overflow: hidden;
  }
  .header-band {
    position: absolute;
    left: 0; top: 0;
    width: 850px;
    height: 39px;
    background: var(--header-red);
  }
  .writing-grid {
    position: absolute;
    left: 0; top: 39px;
    width: 850px;
    height: 1092px;
    background-image:
      linear-gradient(to right, var(--grid-line) 1px, transparent 1px),
      linear-gradient(to bottom, var(--grid-line) 1px, transparent 1px);
    background-size: var(--cell-w) var(--cell-h);
    background-position: 0.5px 0;
  }
  .footer-band {
    position: absolute;
    left: 0; top: 0;
    width: 850px;
    height: 1200px;
    pointer-events: none;
  }
  .footer-band .band-fill { fill: var(--footer-red); }
  .footer-band .band-edge {
    fill: none;
    stroke: var(--edge-dark);
    stroke-width: 3;
  }
  .brand-name {
    position: absolute;
    left: 637px;
    top: 1110px;
    width: 150px;
    font-family: "Archivo", Arial, sans-serif;
    font-weight: 700;
    font-size: 40px;
    line-height: 0.92;
    color: var(--brand-ink);
    text-align: center;
  }
  .brand-name .brand-line {
    display: block;
  }
</style>
</head>
<body>
  <main class="note-sheet">
    <div class="header-band"></div>
    <div class="writing-grid"></div>

    <svg class="footer-band" viewBox="0 0 850 1200" width="850" height="1200" aria-hidden="true">
      <path class="band-fill"
            d="M0,1130 L565,1130 C578,1130 584,1122 589,1110 C595,1095 600,1091 612,1091 L850,1091 L850,1200 L0,1200 Z"/>
      <path class="band-edge"
            d="M0,1130 L565,1130 C578,1130 584,1122 589,1110 C595,1095 600,1091 612,1091 L850,1091"/>
    </svg>

    <div class="brand-name">
      <span class="brand-line">NOTA</span>
      <span class="brand-line">DESK</span>
    </div>
  </main>
</body>
</html>
```